Produce an animated version of our logo

Create an animated version of our logo

I'm looking for our static logo to be converted to an interesting animation that we can use in YouTube videos etc.

I had this idea:
1 - You hear the sound of thunder and a lightning strike briefly reveals the Corvantis logo without the umbrella. (You wouldn't necessarily see the lightening, it might just defect off the wording).
NOTE: As we're animating a static logo I'd like to elevate it, so perhaps a 3D reflective effect on the wording/logo or something appropriate either water droplets on the lens or the wording for the first scene.
2 - You then hear the sound of light rain while the full logo is revealed. The final logo shouldn't have water droplets on the logo.
3 - The sound of rain stops when the logo is fully shown and shows the byline "We've got you covered" below the logo.
4 - The URL is shown Corvantis.com.au

I'm open to other ideas.

I've attached copies of our logo in different formats to assist.

Target Market(s)

Small & medium business owners

Industry/Entity Type

Business Consultant

Font styles to use
Sans Serif

Colors
ec1f27

Requirements
Must have
• - The finished intro shouldn't be more than 6 seconds long.
• - Use dark background using our white & red logo
• - Please see our website Corvantis.com.au to get a sense of our business and style
• - Quality should be 1080p at 30fps
• - Finished product should be MP4 file type
• - In addition to the MP4 please also include the After Effects project & source files in case we need to make changes later on

```html
<!DOCTYPE html>
<html lang="en">
<head>
<meta charset="UTF-8">
<title>Corvantis — Logo Intro Storyboard</title>
<link href="https://fonts.googleapis.com/css2?family=Questrial&family=Arimo:wght@700&display=swap" rel="stylesheet">
<style>
  :root {
    --page-bg: #ffffff;
    --frame-bg: #050505;
    --frame-bg-edge: #0d0d0d;
    --brand-red: #ec1f27;
    --glow-core: #fff4ef;
    --glow-red: rgba(236, 31, 39, 0.85);
    --text-white: #ffffff;
  }
  * { margin: 0; padding: 0; box-sizing: border-box; }
  html, body {
    width: 1200px;
    height: 1200px;
    overflow: hidden;
    background: var(--page-bg);
  }
  .storyboard {
    position: relative;
    width: 1200px;
    height: 1200px;
  }
  .frame {
    position: absolute;
    left: 170px;
    width: 860px;
    height: 483px;
    overflow: hidden;
    background: radial-gradient(ellipse at 50% 50%, var(--frame-bg-edge) 0%, var(--frame-bg) 75%);
  }
  .frame--strike { top: 91px; }
  .frame--reveal { top: 626px; }

  .strike-light {
    position: absolute;
    inset: 0;
    background:
      radial-gradient(circle at 430px 290px, var(--glow-core) 0px, var(--glow-core) 22px, var(--glow-red) 60px, rgba(236,31,39,0.35) 140px, rgba(236,31,39,0) 240px);
  }
  .strike-wordmark {
    position: absolute;
    left: 192px;
    top: 212px;
    font-family: "Questrial", sans-serif;
    font-size: 120px;
    line-height: 1;
    color: var(--text-white);
    letter-spacing: -1px;
  }

  .reveal-lockup {
    position: absolute;
    left: 0;
    right: 0;
    top: 214px;
    text-align: center;
  }
  .brand-name {
    font-family: "Questrial", sans-serif;
    font-size: 84px;
    line-height: 1;
    color: var(--text-white);
    letter-spacing: -1px;
  }
  .brand-tagline {
    margin-top: 4px;
    font-family: "Questrial", sans-serif;
    font-size: 15px;
    letter-spacing: 9.6px;
    color: var(--brand-red);
    text-transform: uppercase;
    padding-left: 9.6px;
  }
  .brand-url {
    position: absolute;
    left: 0;
    right: 0;
    top: 367px;
    text-align: center;
    font-family: "Arimo", sans-serif;
    font-weight: 700;
    font-size: 24px;
    color: var(--text-white);
  }
</style>
</head>
<body>
  <main class="storyboard">
    <section class="frame frame--strike">
      <div class="strike-light" role="img" aria-label="Lightning strike flashing red light across the partially revealed wordmark"></div>
      <div class="strike-wordmark">Cor</div>
    </section>

    <section class="frame frame--reveal">
      <div class="reveal-lockup">
        <div class="brand-name">Corvantis</div>
        <div class="brand-tagline">We've got you covered</div>
      </div>
      <div class="brand-url">Corvantis.com.au</div>
    </section>
  </main>
</body>
</html>
```